Door Hanger Design

I need a design for a door hanger campaign. The door hanger will be 3.5" x 8.5" full color 2 sides. On the first side the emphasis is going to be house painting, exterior and interior. I would really like this to be bold and colorful, I would like to stay away from the standard here is what a painted house looks like.

For the 2nd side I would like the emphasis to be on kitchen and bathroom remodeling. One the front page of our website is a photo of one of our best jobs and if that could be incorporated into side 2 of the door hanger that would be awesome.

The name of our business is Dwelling Brightwell . Our website is http://dwelling-brightwell.example/. We don't currently have a company logo that we use.

I have never done this type of project before. So I'm sure I may be leaving some information out. If you need any questions answered please don't hesitate to contact me. They company that is going to print the designs said that I needed "camera ready artwork" and something about high resolution files.

Industry/Entity Type

House

```html
<!DOCTYPE html>
<html lang="en">
<head>
<meta charset="utf-8">
<title>Dwelling Brightwell – Door Hanger</title>
<link href="https://fonts.googleapis.com/css2?family=VT323&display=swap" rel="stylesheet">
<style>
  :root {
    --paper: #ffffff;
    --red: #ea6b6b;
    --orange: #f28a4a;
    --yellow: #f3e47c;
    --green: #4fb34a;
    --sky: #80cdf0;
    --blue: #3b5fa9;
    --purple: #6c3a8b;
    --house: #a9d13b;
    --brand: #f15a24;
    --ink: #ffffff;
  }
  html, body {
    margin: 0;
    padding: 0;
    overflow: hidden;
    background: var(--paper);
  }
  .hanger {
    position: relative;
    width: 1200px;
    height: 3106px;
    overflow: hidden;
    background: var(--paper);
    font-family: "VT323", monospace;
  }
  .scene {
    position: absolute;
    left: 0;
    top: 1140px;
    width: 1200px;
    height: 1605px;
    background: linear-gradient(180deg, var(--house) 0%, #98c234 70%, #ffffff 100%);
  }
  .paint-stripes {
    position: absolute;
    left: 0;
    top: 0;
    width: 1200px;
    height: 1800px;
  }
  .contact {
    position: absolute;
    writing-mode: vertical-rl;
    transform: rotate(180deg);
    color: var(--ink);
    font-size: 58px;
    line-height: 1;
    letter-spacing: 2px;
    white-space: nowrap;
  }
  .contact--name  { left: 218px; bottom: 2028px; }
  .contact--phone { left: 563px; bottom: 2008px; }
  .contact--email { left: 908px; bottom: 1675px; }
  .brand-band {
    position: absolute;
    left: 0;
    top: 2745px;
    width: 1200px;
    height: 361px;
    background: var(--brand);
  }
  .brand-name {
    position: absolute;
    left: 118px;
    top: 110px;
    width: 964px;
    height: 157px;
    box-sizing: border-box;
    border: 10px solid var(--ink);
    display: flex;
    align-items: center;
    justify-content: center;
    color: var(--ink);
    font-size: 92px;
    letter-spacing: 6px;
    margin: 0;
    font-weight: 400;
  }
</style>
</head>
<body>
  <main class="hanger">
    <div class="scene" role="img" aria-label="Pixel-art painter in blue overalls holding a brush and paint bucket in front of a green house with windows"></div>

    <svg class="paint-stripes" viewBox="0 0 1200 1800" aria-hidden="true">
      <rect x="0"    y="0" width="172" height="1764" fill="var(--red)"/>
      <rect x="172"  y="0" width="172" height="1294" fill="var(--orange)"/>
      <rect x="344"  y="0" width="170" height="1137" fill="var(--yellow)"/>
      <rect x="514"  y="0" width="172" height="1470" fill="var(--green)"/>
      <rect x="686"  y="0" width="170" height="1176" fill="var(--sky)"/>
      <rect x="856"  y="0" width="172" height="1509" fill="var(--blue)"/>
      <rect x="1028" y="0" width="172" height="1646" fill="var(--purple)"/>
    </svg>

    <p class="contact contact--name">Sam Kerwin</p>
    <p class="contact contact--phone">555-014-2298</p>
    <p class="contact contact--email">samkerwin@example.com</p>

    <footer class="brand-band">
      <h1 class="brand-name">DWELLING BRIGHTWELL</h1>
    </footer>
  </main>
</body>
</html>
```